Marn-ridge Tide Harbor Custom Brokers Limited

Name: Dorvella Hastings
Title: Customs Broker
Address: Shop 9 Birchfield Commercial Complex
207-209 Harlow Road
Kingston 8
Telephone: (876)
Email: tideharborport@quillmail.example

```html
<!DOCTYPE html>
<html lang="en">
<head>
<meta charset="utf-8">
<title>Marn-ridge Tide Harbor Custom Brokers Limited — Business Card</title>
<link rel="stylesheet" href="https://fonts.googleapis.com/css2?family=Montserrat:wght@600&family=Source+Sans+3:wght@400;600;700&display=swap">
<style>
  :root {
    --navy: #112d52;
    --gold: #e8a11c;
    --paper: #f4f4f4;
    --backdrop: #e4e4e4;
    --ink: #2a2f38;
    --faint: #e2e2e2;
  }
  html, body {
    margin: 0;
    padding: 0;
    width: 1200px;
    height: 960px;
    overflow: hidden;
    background: var(--backdrop);
  }
  .canvas {
    position: relative;
    width: 1200px;
    height: 960px;
  }
  .card {
    position: absolute;
    left: 318px;
    width: 568px;
    height: 325px;
    overflow: hidden;
  }
  .card--front {
    top: 134px;
    background: var(--navy);
    display: flex;
    align-items: center;
    justify-content: center;
  }
  .card--back {
    top: 508px;
    background: var(--paper);
  }
  .wordmark {
    font-family: "Montserrat", sans-serif;
    font-weight: 600;
    text-align: center;
    letter-spacing: 0.04em;
    line-height: 1.25;
    margin: 0;
  }
  .card--front .wordmark {
    color: #ffffff;
    font-size: 26px;
    width: 360px;
  }
  .card--back .wordmark {
    position: absolute;
    left: 40px;
    top: 560px;
    top: 52px;
    width: 240px;
    color: var(--navy);
    font-size: 19px;
    text-align: left;
  }
  .decor-circle {
    position: absolute;
    right: -70px;
    bottom: -80px;
    width: 260px;
    height: 260px;
    border-radius: 50%;
    background: var(--faint);
  }
  .holder {
    position: absolute;
    right: 33px;
    top: 60px;
    text-align: right;
    font-family: "Source Sans 3", sans-serif;
  }
  .holder__name {
    margin: 0;
    color: var(--navy);
    font-weight: 700;
    font-size: 18px;
    line-height: 1.2;
  }
  .holder__title {
    margin: 2px 0 0;
    color: var(--gold);
    font-size: 14px;
  }
  .contact {
    position: absolute;
    left: 40px;
    top: 186px;
    font-family: "Source Sans 3", sans-serif;
    font-size: 14.5px;
    color: var(--ink);
    line-height: 19px;
  }
  .contact__address {
    margin: 0 0 10px;
    font-style: normal;
  }
  .contact__line {
    display: flex;
    align-items: center;
    gap: 5px;
    margin: 0;
  }
  .contact__icon {
    width: 13px;
    height: 13px;
    flex: none;
  }
</style>
</head>
<body>
<main class="canvas">
  <section class="card card--front" aria-label="Card front">
    <p class="wordmark">Marn-ridge Tide Harbor Custom Brokers Limited</p>
  </section>

  <section class="card card--back" aria-label="Card back">
    <div class="decor-circle" aria-hidden="true"></div>
    <p class="wordmark">Marn-ridge Tide Harbor Custom Brokers Limited</p>

    <div class="holder">
      <p class="holder__name">Dorvella Hastings</p>
      <p class="holder__title">Customs Broker</p>
    </div>

    <div class="contact">
      <address class="contact__address">
        Shop 9 Birchfield Commercial Complex<br>
        207-209 Harlow Road<br>
        Kingston 8
      </address>
      <p class="contact__line">
        <svg class="contact__icon" viewBox="0 0 24 24" aria-hidden="true"><path fill="#e8a11c" d="M6.6 10.8a15.1 15.1 0 0 0 6.6 6.6l2.2-2.2a1 1 0 0 1 1-.25 11.4 11.4 0 0 0 3.6.57 1 1 0 0 1 1 1V20a1 1 0 0 1-1 1A17 17 0 0 1 3 4a1 1 0 0 1 1-1h3.5a1 1 0 0 1 1 1c0 1.25.2 2.45.57 3.57a1 1 0 0 1-.25 1z"/></svg>
        (876) 555-0148
      </p>
      <p class="contact__line">
        <svg class="contact__icon" viewBox="0 0 24 24" aria-hidden="true"><rect x="2.5" y="5" width="19" height="14" rx="1" fill="none" stroke="#e8a11c" stroke-width="2"/><path d="M3 6l9 7 9-7" fill="none" stroke="#e8a11c" stroke-width="2"/></svg>
        tideharborport@quillmail.example
      </p>
    </div>
  </section>
</main>
</body>
</html>
```